Design Business Cards for Recruitment company

Hello, I need a creative design for business cards for a recruitment company. I am looking for something modern, not traditional. We would like to use UV varnish technology for printing (inspiration: http://lnkvault.example/7QzR2Tw).

The business card has to be delivered IN PRINGING PDF format!
You can find our logo in the attachment.
The cards will have 2 different names on it.

1st TEXT:
Ing. Lenka Farkašová, PhD.
Director
MORAVIA TALENTS, spol. s r. o.
www.moravia-talents.example
+421/(0) 915 274 503
lenka.farkasova@moravia-talents.example

2nd TEXT:
Ing. Zuzana Hrdličková
Consultant
www.moravia-talents.example
+421/(0) 907 615 241
zuzana.hrdlickova@moravia-talents.example

```html
<!DOCTYPE html>
<html lang="sk">
<head>
<meta charset="utf-8">
<title>Moravia Talents – vizitky</title>
<link rel="stylesheet" href="https://fonts.googleapis.com/css2?family=Lato:wght@400;700&display=swap">
<style>
  :root {
    --backdrop: #2a2a2c;
    --card-white: #f2f2f0;
    --card-green: #78c043;
    --ink: #2e2e2e;
    --ink-soft: #5a5a5a;
    --accent: #6cb83a;
    --on-green: #f4fbef;
  }
  * { margin: 0; padding: 0; box-sizing: border-box; }
  html, body {
    width: 1200px; height: 900px; overflow: hidden;
    background: var(--backdrop);
    font-family: "Lato", sans-serif;
  }
  .stage { position: relative; width: 1200px; height: 900px; }

  .card {
    position: absolute;
    width: 630px; height: 360px;
    border-radius: 4px;
  }

  /* Front: personal details */
  .card-front {
    left: 110px; top: 110px;
    background: var(--card-white);
    display: flex; align-items: center;
    padding: 0 44px;
  }
  .front-brand { width: 250px; }
  .brand-name {
    font-weight: 700; color: var(--ink);
    letter-spacing: 0.08em; line-height: 1.15;
  }
  .card-front .brand-name { font-size: 26px; }
  .details { flex: 1; padding-left: 20px; color: var(--ink); }
  .person-name {
    font-size: 19px; font-weight: 700;
    padding-bottom: 4px;
    border-bottom: 3px solid var(--accent);
    display: inline-block;
  }
  .person-role {
    font-size: 12px; font-weight: 700; letter-spacing: 0.12em;
    margin-top: 6px; color: var(--ink-soft);
  }
  .contact { margin-top: 34px; font-size: 13px; line-height: 1.55; color: var(--ink-soft); }
  .contact .web { color: var(--accent); }

  /* Back: brand side */
  .card-back {
    left: 460px; top: 430px;
    background: var(--card-green);
    display: flex; flex-direction: column;
    align-items: center; justify-content: center;
  }
  .card-back .brand-name { font-size: 44px; text-align: center; }
  .back-web {
    position: absolute; bottom: 46px;
    font-size: 17px; letter-spacing: 0.04em; color: var(--on-green);
  }
</style>
</head>
<body>
<main class="stage">
  <section class="card card-front">
    <div class="front-brand">
      <p class="brand-name">MORAVIA<br>TALENTS</p>
    </div>
    <div class="details">
      <p class="person-name">Ing. Lenka Farkašová, PhD.</p>
      <p class="person-role">Director</p>
      <div class="contact">
        <p>MORAVIA TALENTS, spol. s r. o.</p>
        <p>+421/(0) 915 274 503</p>
        <p>lenka.farkasova@moravia-talents.example</p>
        <p class="web">www.moravia-talents.example</p>
      </div>
    </div>
  </section>

  <section class="card card-back">
    <p class="brand-name">MORAVIA<br>TALENTS</p>
    <p class="back-web">www.moravia-talents.example</p>
  </section>
</main>
</body>
</html>
```